Faithful in the Small...Powerful together

Capital Campaign for Meadowlight Church...need it engaging..spiritually based with pics of the community etc...

Target Market(s)

church congregation and sphere of influence

Industry/Entity Type

religious

Colors
EB3D1F
EC4F4E
F09395
F8D3D4
FCEDEE

Requirements
Must have
• tier levels..engaging scripture and photos

```html
<!DOCTYPE html>
<html lang="en">
<head>
<meta charset="utf-8">
<title>Meadowlight Church – Faithful in the Small, Powerful Together</title>
<link href="https://fonts.googleapis.com/css2?family=Rubik:wght@400;500;600;700&family=Saira+Condensed:wght@700;800&family=Yellowtail&display=swap" rel="stylesheet">
<style>
  :root{
    --red:#e01b22;
    --red-bright:#eb3d1f;
    --rose:#ec4f4e;
    --pink:#f09395;
    --blush:#f8d3d4;
    --mist:#fcedee;
    --ink:#1f1f1f;
    --night:#161616;
    --stage:#a3a3a3;
    --white:#ffffff;
  }
  *{box-sizing:border-box;margin:0;padding:0}
  html,body{width:1051px;height:1200px;overflow:hidden}
  body{background:var(--stage);font-family:"Rubik",sans-serif;color:var(--ink);position:relative}

  .spread{position:absolute;left:191px;width:669px;height:518px;overflow:hidden}
  .spread--outside{top:67px}
  .spread--inside{top:614px}
  .spread__backdrop{position:absolute;inset:0;background:linear-gradient(180deg,#2a2a2a 0%,#141414 55%,#1d1d1d 100%)}
  .spread__half{position:absolute;top:0;bottom:0;left:334px;right:0;background:linear-gradient(180deg,#232323 0%,#121212 60%,#1a1a1a 100%)}

  .card{position:absolute;background:var(--white);border-radius:17px;overflow:hidden}
  .abs{position:absolute}

  /* Giving model card */
  .model{left:24px;top:25px;width:285px;height:468px}
  .model__title{left:0;right:0;top:22px;text-align:center;color:var(--red);font-weight:700;font-size:14.5px;letter-spacing:-.1px}
  .model__lead{left:20px;right:20px;top:41px;text-align:center;font-size:10.8px;line-height:14px}
  .tiers{left:24px;top:75px;width:238px;border:1px solid #9a9a9a;border-radius:4px;overflow:hidden}
  .tiers__band{background:var(--red);color:var(--white);text-align:center;font-weight:700;font-size:14.5px;height:23px;line-height:24px}
  .tiers table{width:100%;border-collapse:collapse;font-size:9.6px}
  .tiers th,.tiers td{border-right:1px solid #9a9a9a;border-bottom:1px solid #9a9a9a;text-align:center}
  .tiers th:last-child,.tiers td:last-child{border-right:none}
  .tiers tr:last-child td{border-bottom:none}
  .tiers th{font-weight:600;height:20px;font-size:9.6px}
  .tiers td{height:30.5px;font-size:10.2px}
  .tiers td.tiers__group{text-align:left;padding-left:8px;font-size:8.6px;line-height:11px}
  .tiers tr.tiers__total td{height:29px;font-weight:400}
  .tiers td.tiers__sum-label{text-align:right;padding-right:15px;font-weight:600;font-size:10.8px}
  .model__margin{left:24px;top:292px;font-size:11px;font-weight:500}
  .reasons{top:311px;left:24px;right:10px;font-size:11px;line-height:14.5px}
  .reason{position:absolute;top:0;padding-left:12px}
  .reason svg{position:absolute;left:0;top:3px;width:8px;height:8px}

  .contact{left:4px;top:360px;width:278px;height:104px;background:var(--red);border-radius:0 0 14px 14px;color:var(--white)}
  .contact__title{left:19px;top:17px;font-weight:700;font-size:11.5px;text-decoration:underline;text-underline-offset:2px}
  .contact__line{left:21px;font-size:8.4px;line-height:11px;padding-left:14px}
  .contact__line svg{position:absolute;left:0;top:1.5px;width:9px;height:9px}
  .contact__mark{left:167px;top:14px;width:90px;height:76px;background:var(--white);display:flex;flex-direction:column;align-items:center;justify-content:center;gap:3px;color:var(--red);font-weight:700;font-size:11px;text-align:center;line-height:12px}
  .mark-dot{width:10px;height:10px;border-radius:50%;background:var(--red)}

  /* Cover */
  .cover{left:334px;top:0;right:0;bottom:0}
  .cover__brand{left:0;right:0;top:50px;text-align:center;color:var(--white);font-weight:600;font-size:23px;line-height:26px}
  .cover__brand small{display:block;font-size:11px;letter-spacing:1.5px;line-height:14px;font-weight:600}
  .cover__brand .mark-dot{margin:0 auto 6px;width:14px;height:14px}
  .cover__headline{left:0;right:0;top:151px;text-align:center;color:var(--white);font-family:"Saira Condensed",sans-serif;font-weight:800;font-size:31px;line-height:36px;letter-spacing:.2px}
  .cover__goal{left:62px;top:229px;width:212px;height:25px;border-radius:13px;background:var(--red);color:#1a1a1a;font-family:"Saira Condensed",sans-serif;font-weight:800;font-size:17px;line-height:26px;text-align:center}
  .cover__photo{left:0;top:273px;width:335px;height:245px}

  /* Inside cards */
  .vision{left:24px;top:25px;width:285px;height:468px}
  .stories{left:359px;top:25px;width:285px;height:468px}
  .heading{color:var(--red);font-weight:700}
  .heading--xl{font-size:14.5px}
  .heading--md{font-size:10.6px}
  .photo{position:absolute}
  .fact{left:24px;font-size:9.4px;line-height:12px}
  .fact b{font-weight:500;text-decoration:underline}
  .vision__body{left:149px;top:166px;width:113px;font-size:8.4px;line-height:11px;text-align:justify}
  .motto{left:149px;font-family:"Yellowtail",cursive;color:var(--red);font-size:14.5px;line-height:15px}
  .verse{top:390px;height:56px;border:1px solid var(--red);border-radius:6px;font-size:8.3px;line-height:11px;padding:11px 9px 0}
  .verse__open,.verse__close{position:absolute;color:var(--red);font-family:"Saira Condensed",sans-serif;font-weight:800;font-size:14px;line-height:10px;background:var(--white)}
  .verse__open{left:-2px;top:-4px;padding-right:2px}
  .verse__ref{position:absolute;right:12px;bottom:-6px;background:var(--white);padding:0 3px;font-size:8.3px;font-weight:600;line-height:11px}
  .verse__ref span{color:var(--red);font-family:"Saira Condensed",sans-serif;font-weight:800;font-size:13px}

  .story{left:25px;width:143px;font-size:7.7px;line-height:10.2px;text-align:justify}
  .wide{left:25px;width:237px;font-size:7.7px;line-height:10.2px}
  .commitment{left:25px;top:268px;width:236px;height:72px;border:1px solid var(--red);border-radius:7px;padding:6px 12px 0 13px}
  .commitment p{font-size:7.6px;line-height:10px;text-align:justify;margin-top:2px}
  .join{left:25px;top:354px;font-size:11px;text-decoration:underline;text-underline-offset:2px}
  .act{position:absolute;display:flex;align-items:center;gap:4px;font-size:8.4px;font-weight:500;line-height:9.5px}
  .act__icon{width:18px;height:18px;border-radius:50%;background:var(--red);flex:none;display:flex;align-items:center;justify-content:center}
  .act__icon svg{width:10px;height:10px}
</style>
</head>
<body>

<section class="spread spread--outside">
  <div class="spread__backdrop" role="img" aria-label="Darkened photo of a steel river bridge behind the page"></div>
  <div class="spread__half"></div>

  <article class="card model">
    <h2 class="abs model__title">REALISTIC PARTICIPATION MODEL</h2>
    <p class="abs model__lead">Not everyone will give equally—so let’s build a real-world scenario:</p>

    <div class="abs tiers">
      <div class="tiers__band">TIERED GIVING PLAN</div>
      <table>
        <colgroup><col style="width:61px"><col style="width:46px"><col style="width:67px"><col></colgroup>
        <tr><th>Group</th><th>People</th><th>Weekly Gift</th><th>Yearly Total</th></tr>
        <tr><td class="tiers__group">Leadership<br>Givers</td><td>10</td><td>$100</td><td>$52,000</td></tr>
        <tr><td class="tiers__group">Core Givers</td><td>40</td><td>$40</td><td>$83,200</td></tr>
        <tr><td class="tiers__group">Consistent<br>Givers</td><td>60</td><td>$20</td><td>$62,400</td></tr>
        <tr><td class="tiers__group">Entry Givers</td><td>40</td><td>$10</td><td>$20,800</td></tr>
        <tr class="tiers__total"><td class="tiers__sum-label" colspan="3">Total:</td><td>$218,400</td></tr>
      </table>
    </div>

    <p class="abs model__margin">This exceeds the goal, giving margin for:</p>
    <div class="abs reasons">
      <div class="reason" style="left:0">
        <svg viewBox="0 0 10 10"><circle cx="5" cy="5" r="5" fill="#e01b22"/><path d="M2.6 5.2l1.6 1.6 3.2-3.4" stroke="#fff" stroke-width="1.4" fill="none"/></svg>
        Missed<br>weeks</div>
      <div class="reason" style="left:67px">
        <svg viewBox="0 0 10 10"><circle cx="5" cy="5" r="5" fill="#e01b22"/><path d="M2.6 5.2l1.6 1.6 3.2-3.4" stroke="#fff" stroke-width="1.4" fill="none"/></svg>
        Lower<br>participation</div>
      <div class="reason" style="left:152px">
        <svg viewBox="0 0 10 10"><circle cx="5" cy="5" r="5" fill="#e01b22"/><path d="M2.6 5.2l1.6 1.6 3.2-3.4" stroke="#fff" stroke-width="1.4" fill="none"/></svg>
        Unexpected<br>needs</div>
    </div>

    <div class="abs contact">
      <h3 class="abs contact__title">CONTACT &nbsp;US</h3>
      <p class="abs contact__line" style="top:39px">
        <svg viewBox="0 0 10 10"><circle cx="5" cy="5" r="5" fill="#1a1a1a"/><path d="M5 2.2a1.8 1.8 0 0 1 1.8 1.8c0 1.3-1.8 3.4-1.8 3.4S3.2 5.3 3.2 4A1.8 1.8 0 0 1 5 2.2z" fill="#e01b22"/></svg>
        1180 Harbor Ridge Road<br>Fairmont, Tennessee 37000</p>
      <p class="abs contact__line" style="top:63px">
        <svg viewBox="0 0 10 10"><circle cx="5" cy="5" r="5" fill="#1a1a1a"/><path d="M3.2 2.6l1 .1.5 1.3-.6.5a3.4 3.4 0 0 0 1.4 1.4l.5-.6 1.3.5.1 1c-.3.4-.8.6-1.3.5A4.4 4.4 0 0 1 2.7 3.9c-.1-.5.1-1 .5-1.3z" fill="#e01b22"/></svg>
        555.014.2290</p>
      <p class="abs contact__line" style="top:77px">
        <svg viewBox="0 0 10 10"><circle cx="5" cy="5" r="5" fill="#1a1a1a"/><circle cx="5" cy="5" r="2.8" stroke="#e01b22" stroke-width=".8" fill="none"/><path d="M2.2 5h5.6M5 2.2c-1.4 1.6-1.4 4 0 5.6M5 2.2c1.4 1.6 1.4 4 0 5.6" stroke="#e01b22" stroke-width=".7" fill="none"/></svg>
        www.meadowlightchurch.org</p>
      <div class="abs contact__mark"><span class="mark-dot"></span>Meadowlight<br>Church</div>
    </div>
  </article>

  <div class="abs cover">
    <div class="abs cover__brand"><span class="mark-dot"></span>Meadowlight<small>CHURCH</small></div>
    <h1 class="abs cover__headline">FAITHFUL IN THE SMALL,<br>POWERFUL TOGETHER.</h1>
    <p class="abs cover__goal">GOAL: $150,000 in 12 Months</p>
    <svg class="abs cover__photo" viewBox="0 0 335 245" role="img" aria-label="Photo of three smiling church volunteers with a shopping cart full of donated groceries">
      <defs>
        <linearGradient id="volunteers" x1="0" y1="0" x2="1" y2="1">
          <stop offset="0" stop-color="#8f8a86"/>
          <stop offset=".35" stop-color="#d9b8ae"/>
          <stop offset=".6" stop-color="#9bb8d8"/>
          <stop offset="1" stop-color="#5f6f86"/>
        </linearGradient>
      </defs>
      <path d="M8 245C4 175 45 120 120 100C200 78 290 70 335 0V245Z" fill="#e01b22"/>
      <path d="M15 245C12 180 52 128 125 108C205 86 295 80 335 14V245Z" fill="#ffffff"/>
      <path d="M19 245C17 183 56 132 128 112C208 90 298 86 335 22V245Z" fill="url(#volunteers)"/>
    </svg>
  </div>
</section>

<section class="spread spread--inside">
  <div class="spread__backdrop" role="img" aria-label="Darkened photo of a steel river bridge behind the page"></div>
  <div class="spread__half"></div>

  <article class="card vision">
    <h2 class="abs heading heading--xl" style="left:24px;top:28px;text-decoration:underline;text-underline-offset:2px">BIG PICTURE</h2>
    <p class="abs fact" style="top:43px"><b>TOTAL GOAL:</b> $150,000</p>
    <p class="abs fact" style="top:60px"><b>ACTIVE MEMBERS:</b><br>Approximately 150 people</p>
    <p class="abs fact" style="top:89px"><b>TIMEFRAME:</b> 12 months</p>
    <p class="abs fact" style="top:109px">That is $1,000 per person<br>per year on average.</p>
    <div class="photo" style="left:149px;top:24px;width:112px;height:106px;background:linear-gradient(135deg,#3b3f5a,#b9a7a8 55%,#6f7f8f)" role="img" aria-label="Photo of church members praying together with hands on one another’s shoulders"></div>

    <div class="photo" style="left:24px;top:150px;width:113px;height:220px;background:linear-gradient(180deg,#5d8fd0 0%,#9fbde4 35%,#b58d78 62%,#8a7a52 100%)" role="img" aria-label="Photo of the church building with a white steeple and a Love, Live, Lead like Him banner flag in front"></div>

    <h3 class="abs heading heading--md" style="left:149px;top:152px">The Heart of the Vision</h3>
    <p class="abs vision__body">We are restoring more than space. We are restoring a church where we</p>
    <p class="abs motto" style="top:206px">Love like Him</p>
    <p class="abs motto" style="top:221px">Live like Him</p>
    <p class="abs motto" style="top:237px">Lead like Him</p>

    <div class="photo" style="left:149px;top:255px;width:112px;height:115px;background:linear-gradient(160deg,#4a4148,#a08a82 50%,#5a5f6e)" role="img" aria-label="Photo of two women embracing during a worship service"></div>

    <blockquote class="abs verse" style="left:24px;width:113px">
      <span class="verse__open">“</span>
      Whoever is faithful in very little is also faithful in much.
      <cite class="verse__ref">Luke 16:10 <span>–”</span></cite>
    </blockquote>
    <blockquote class="abs verse" style="left:149px;width:112px">
      <span class="verse__open">“</span>
      How good &amp; pleasant it is when God’s people live together in unity.
      <cite class="verse__ref">Psalm 133:1 <span>–”</span></cite>
    </blockquote>
  </article>

  <article class="card stories">
    <h2 class="abs heading heading--md" style="left:25px;top:23px">Stories of What God Is Doing</h2>
    <p class="abs story" style="top:37px">One Wednesday night, a woman went to visit another church, but they were closed for a break. Instead of turning back, she came here. That unexpected moment became a divine appointment. God brought her to Meadowlight.</p>
    <p class="abs story" style="top:103px">Another couple walked through our doors carrying deep church hurt. From the very first moment, they felt seen, valued, &amp; welcomed. What they found here was not just a service, but a family.</p>
    <p class="abs story" style="top:159px">This is what we are building together.</p>
    <div class="photo" style="left:184px;top:24px;width:78px;height:139px;background:linear-gradient(170deg,#7a6a4e,#8aa2c6 55%,#5f7a5a)" role="img" aria-label="Photo of the pastor in a light blue jacket speaking with a congregation member"></div>
    <p class="abs wide" style="top:174px;text-align:justify">These gifts help build momentum, inspire others, and move the vision forward in powerful ways.</p>

    <h2 class="abs heading heading--md" style="left:25px;top:205px">How We Move Forward Together</h2>
    <p class="abs wide" style="top:219px">We encourage<br>Everyone to participate, even one dollar a day matters Some to give stretch gifts as they are able A few to provide leadership gifts to help anchor the campaign</p>

    <div class="abs commitment">
      <h3 class="heading heading--md">A Shared Commitment</h3>
      <p>“If each of us gave just $20 a week, we would not only meet our goal, we would exceed it. But this is not about equal giving. It is about equal sacrifice. Some can give more, some less, but together, we can do something powerful.”</p>
    </div>

    <h2 class="abs heading join">JOIN US</h2>
    <div class="act" style="left:25px;top:368px">
      <span class="act__icon"><svg viewBox="0 0 10 10"><circle cx="5" cy="2" r="1.2" fill="#fff"/><path d="M5 3.6v3.4M3 4.2 5 5.4 7 4.2M3.8 9 5 7l1.2 2" stroke="#fff" stroke-width=".9" fill="none"/></svg></span>Pray</div>
    <div class="act" style="left:76px;top:368px">
      <span class="act__icon"><svg viewBox="0 0 10 10"><path d="M3 4a2.2 2.2 0 1 1 4.2 1c-.5.8-1.4 1.2-1.4 2.2 0 .9-.6 1.5-1.4 1.5" stroke="#fff" stroke-width=".9" fill="none"/><path d="M4.4 4.2a.8.8 0 1 1 1.4.6" stroke="#fff" stroke-width=".8" fill="none"/></svg></span>Listen</div>
    <div class="act" style="left:25px;top:391px">
      <span class="act__icon"><svg viewBox="0 0 10 10"><path d="M1.5 6 4 8.5h2L8.5 6M3 6V3.2M7 6V3.2M3 3.2 5 5.2 7 3.2" stroke="#fff" stroke-width=".9" fill="none"/></svg></span>Listen Step forward<br>in faith</div>
    <p class="abs" style="left:25px;top:415px;width:105px;font-size:8.3px;line-height:10.5px">Together, we believe God will do more than we can ask or imagine.</p>
    <div class="photo" style="left:136px;top:354px;width:126px;height:90px;background:linear-gradient(160deg,#9aa0a2,#c9c8c2 45%,#6c6f70)" role="img" aria-label="Photo of three volunteers preparing trays of food in the church kitchen"></div>
  </article>
</section>

</body>
</html>
```